Quilvo Garage Doors Business Card

I need a Business Card for my garage door business:
Quilvo Garage Doors.
please add:
logo
phone number: 855-3-QUILVO
(853-392)

email: service@quilvogaragedoors.com
website: www.quilvogaragedoors.com

The attached image is recommendation ONLY.

```html
<!DOCTYPE html>
<html lang="en">
<head>
<meta charset="utf-8">
<title>Quilvo Garage Doors Business Card</title>
<link href="https://fonts.googleapis.com/css2?family=Lato:wght@400;700;900&display=swap" rel="stylesheet">
<style>
  :root {
    --page: #2b2b2d;
    --teal: #4db3c0;
    --teal-deep: #3a9fad;
    --teal-light: #6ec7d2;
    --ink: #1f2326;
    --grey: #5a6166;
    --white: #ffffff;
    --paper: #f4f5f5;
  }
  * { box-sizing: border-box; margin: 0; padding: 0; }
  html, body { width: 1200px; height: 997px; overflow: hidden; }
  body {
    background: var(--page);
    font-family: "Lato", sans-serif;
    position: relative;
  }
  .card {
    position: absolute;
    left: 340px;
    width: 520px;
    height: 300px;
    border-radius: 16px;
    overflow: hidden;
  }

  /* Front */
  .card-front { top: 140px; background: var(--paper); }
  .front-brand {
    position: absolute; left: 150px; top: 50px;
    display: flex; align-items: center; gap: 16px;
  }
  .brand-mark {
    width: 56px; height: 56px; border-radius: 10px; background: var(--teal);
  }
  .brand-name {
    font-weight: 700; font-size: 30px; color: var(--ink); line-height: 1.05;
  }
  .front-rule {
    position: absolute; left: 0; right: 0; top: 143px; height: 4px; background: var(--ink);
  }
  .front-band {
    position: absolute; left: 0; right: 0; top: 147px; height: 95px; background: var(--teal);
  }
  .contact-list {
    position: absolute; right: 22px; top: 12px; text-align: right;
    list-style: none; color: var(--ink); font-size: 13px; line-height: 22px;
  }
  .contact-list svg { vertical-align: -2px; margin-left: 6px; }
  .holder {
    position: absolute; left: 24px; bottom: 10px; color: var(--white);
  }
  .holder-name { font-weight: 700; font-size: 17px; }
  .holder-role { font-size: 13px; color: var(--ink); }
  .holder-notch {
    position: absolute; left: 28px; top: 0; width: 0; height: 0;
    border-left: 10px solid transparent; border-right: 10px solid transparent;
    border-top: 10px solid var(--ink);
  }
  .quote-strip {
    position: absolute; left: 0; right: 0; top: 242px; height: 34px;
    background: var(--white); color: var(--ink);
    font-size: 14px; letter-spacing: 1.5px; text-align: center; line-height: 34px;
  }
  .front-foot {
    position: absolute; left: 0; right: 0; top: 276px; bottom: 0; background: var(--teal);
  }

  /* Back */
  .card-back { top: 520px; color: var(--white); }
  .back-surface {
    position: absolute; inset: 0;
    background: linear-gradient(135deg, var(--teal-light) 0%, var(--teal) 50%, var(--teal-deep) 100%);
  }
  .back-brand {
    position: absolute; left: 150px; top: 26px;
    display: flex; align-items: center; gap: 16px;
  }
  .back-brand .brand-mark { background: var(--white); width: 50px; height: 50px; }
  .back-brand .brand-name { font-size: 26px; }
  .services {
    position: absolute; left: 0; right: 0; top: 104px;
    display: flex; justify-content: space-around; text-align: center; list-style: none;
  }
  .service { width: 150px; }
  .service-icon { height: 46px; display: flex; justify-content: center; align-items: center; margin-bottom: 6px; }
  .service-square { width: 40px; height: 40px; border: 4px solid var(--white); border-radius: 4px; }
  .service-title { font-weight: 900; font-size: 15px; }
  .service-note { font-size: 12px; }
  .discount {
    position: absolute; left: 0; right: 0; top: 222px; text-align: center;
    font-size: 16px; color: var(--ink);
  }
  .website {
    position: absolute; left: 0; right: 0; top: 252px; text-align: center;
    font-weight: 700; font-size: 15px; letter-spacing: 4px;
  }
</style>
</head>
<body>

<section class="card card-front" aria-label="Business card front">
  <div class="front-brand">
    <span class="brand-mark"></span>
    <span class="brand-name">Quilvo<br>Garage Doors</span>
  </div>
  <div class="front-rule"></div>
  <div class="front-band">
    <ul class="contact-list">
      <li>855-3-QUILVO (853-392)
        <svg width="13" height="12" viewBox="0 0 13 12"><path d="M3 1 L5 3 L4 5 Q6 8 8 8 L10 7 L12 9 L10 11 Q2 11 1 3 Z" fill="var(--white)"/></svg>
      </li>
      <li>service@quilvogaragedoors.com
        <svg width="13" height="10" viewBox="0 0 13 10"><rect x="0.5" y="0.5" width="12" height="9" fill="var(--white)"/><path d="M0.5 0.5 L6.5 5.5 L12.5 0.5" stroke="var(--teal)" fill="none"/></svg>
      </li>
    </ul>
    <div class="holder">
      <p class="holder-name">Daniel Korvath</p>
      <p class="holder-role">Owner / Founder</p>
    </div>
    <span class="holder-notch"></span>
  </div>
  <p class="quote-strip">Call us for no obligation Free Quote</p>
  <div class="front-foot"></div>
</section>

<section class="card card-back" aria-label="Business card back">
  <div class="back-surface" role="img" aria-label="Teal low-poly faceted background texture"></div>
  <div class="back-brand">
    <span class="brand-mark"></span>
    <span class="brand-name">Quilvo<br>Garage Doors</span>
  </div>
  <ul class="services">
    <li class="service">
      <div class="service-icon"><span class="service-square"></span></div>
      <p class="service-title">GARAGE DOOR</p>
      <p class="service-note">Installation</p>
    </li>
    <li class="service">
      <div class="service-icon">
        <svg width="70" height="46" viewBox="0 0 70 46">
          <circle cx="24" cy="26" r="12" fill="none" stroke="var(--white)" stroke-width="8" stroke-dasharray="5 4"/>
          <circle cx="24" cy="26" r="9" fill="none" stroke="var(--white)" stroke-width="5"/>
          <circle cx="50" cy="14" r="8" fill="none" stroke="var(--white)" stroke-width="6" stroke-dasharray="4 3"/>
          <circle cx="50" cy="14" r="6" fill="none" stroke="var(--white)" stroke-width="4"/>
        </svg>
      </div>
      <p class="service-title">OPENERS</p>
      <p class="service-note">Garage Door Openers</p>
    </li>
    <li class="service">
      <div class="service-icon">
        <svg width="50" height="46" viewBox="0 0 50 46">
          <path d="M8 10 L40 40" stroke="var(--white)" stroke-width="6" stroke-linecap="round"/>
          <circle cx="8" cy="10" r="7" fill="var(--white)"/>
          <path d="M38 6 L14 38" stroke="var(--white)" stroke-width="5" stroke-linecap="round"/>
          <path d="M40 4 L44 0" stroke="var(--white)" stroke-width="2"/>
        </svg>
      </div>
      <p class="service-title">REPAIR SERVICE</p>
      <p class="service-note">24*7 No Extra Charge</p>
    </li>
  </ul>
  <p class="discount">To avail special discounts pl log into</p>
  <p class="website">www.quilvogaragedoors.com</p>
</section>

</body>
</html>
```